New Company Business Card Design

I have a new company logo and I want a new business card design. I dont know if the logo file i attached is in the correct format or quality. We are a New York City Specialty construction Firm specializing in high risk out of the box projects. I want a simple and classy business card that people will his card is as crisp as the work his company does.

Target Market(s)

Clients in the heavy construction industry in New York City

Industry/Entity Type

Construction Company

Contact Information for Business Card

Simple Classy - DIFFERENT

Font styles to use
Other font styles liked:
• Mach the logo font in some way

Colors

Designer to choose colors to be used in the design.

Requirements
Must have
• Uniqueness
Nice to have
• Nothing particular - Just different and classy - Timeless
Should not have
• Goofy Shit or Gimmicky shit

```html
<!DOCTYPE html>
<html lang="en">
<head>
<meta charset="utf-8">
<title>Kord Builders — Business Cards</title>
<link href="https://fonts.googleapis.com/css2?family=Montserrat:wght@400;500;700;800&display=swap" rel="stylesheet">
<style>
  :root {
    --board: #bdbec0;
    --paper: #ffffff;
    --map-tone: #e9e9ea;
    --ink: #222226;
    --brand: #1c63b3;
    --navy: #1e3f8c;
    --sky: #1ea0e0;
    --onyx: #111114;
    --onyx-deep: #060609;
  }
  * { margin: 0; padding: 0; box-sizing: border-box; }
  html, body { width: 1200px; height: 778px; overflow: hidden; }
  body {
    background: var(--board);
    font-family: "Montserrat", sans-serif;
    color: var(--ink);
    position: relative;
  }
  .card {
    position: absolute;
    width: 518px;
    height: 295px;
    background: var(--paper);
    box-shadow: 0 2px 8px rgba(0,0,0,.18);
    overflow: hidden;
  }
  .card--front-light { left: 62px; top: 62px; }
  .card--back-right  { left: 620px; top: 62px; }
  .card--front-dark  { left: 62px; top: 420px; background: var(--onyx); }
  .card--back-left   { left: 620px; top: 420px; }

  .map-texture {
    position: absolute; inset: 0;
    background: linear-gradient(135deg, #f0f0f1 0%, var(--map-tone) 55%, #dedfe0 100%);
  }

  .wordmark {
    position: absolute;
    font-weight: 800;
    color: var(--brand);
    line-height: 1;
    text-align: center;
  }
  .wordmark__name { display: block; letter-spacing: 2px; }
  .wordmark__suffix { display: block; letter-spacing: 5px; }

  .card--front-light .wordmark { left: 0; right: 0; top: 82px; }
  .card--front-light .wordmark__name { font-size: 72px; }
  .card--front-light .wordmark__suffix { font-size: 15px; margin-top: 10px; }

  .front-url {
    position: absolute; left: 0; right: 0; top: 258px;
    text-align: center; font-weight: 800; font-size: 18px;
    color: var(--navy); letter-spacing: .5px;
  }

  .card--front-dark .wordmark { left: 0; right: 0; top: 100px; color: var(--onyx-deep); }
  .card--front-dark .wordmark__name { font-size: 92px; }
  .card--front-dark .wordmark__suffix { font-size: 18px; margin-top: 14px; }

  .card--back-right .wordmark { left: 30px; top: 38px; text-align: left; }
  .card--back-right .wordmark__name { font-size: 58px; }
  .card--back-right .wordmark__suffix { font-size: 12px; margin-top: 8px; }

  .stripe-v {
    position: absolute; top: 0; bottom: 0;
    background: linear-gradient(180deg, var(--sky), var(--navy));
  }
  .card--back-right .stripe-v { left: 484px; width: 8px; }
  .card--back-left .stripe-v { left: 0; width: 10px; }

  .person__name { font-weight: 800; font-size: 19px; color: var(--navy); letter-spacing: -.2px; }
  .person__title { font-size: 13px; font-weight: 500; margin-top: 2px; }

  .card--back-right .person { position: absolute; right: 48px; top: 142px; text-align: right; }

  .contact-stack { position: absolute; right: 22px; top: 194px; list-style: none; }
  .contact-stack li {
    display: flex; justify-content: flex-end; align-items: center;
    height: 21.5px; font-size: 13px; letter-spacing: .8px;
  }
  .contact-stack .ico-box {
    width: 18px; height: 18px; margin-left: 8px;
    border: 1.5px solid var(--ink); background: #fff;
    display: flex; align-items: center; justify-content: center;
  }
  .ico { width: 11px; height: 11px; fill: var(--ink); }

  .card--back-left .wordmark { left: 302px; width: 196px; top: 36px; }
  .card--back-left .wordmark__name { font-size: 56px; }
  .card--back-left .wordmark__suffix { font-size: 11px; margin-top: 8px; letter-spacing: 4px; }
  .card--back-left .person { position: absolute; left: 32px; top: 136px; }

  .contact-list { position: absolute; left: 302px; top: 136px; width: 196px; list-style: none; }
  .contact-list li {
    display: flex; align-items: flex-start;
    font-size: 13px; font-weight: 500;
    padding: 4px 0 3px; border-bottom: 1.5px solid var(--ink);
    line-height: 1.2;
  }
  .contact-list .ico { margin: 2px 6px 0 1px; flex: none; }
</style>
</head>
<body>

<section class="card card--front-light">
  <div class="map-texture" role="img" aria-label="Faint street map of the city as card background"></div>
  <div class="wordmark">
    <span class="wordmark__name">KORD</span>
    <span class="wordmark__suffix">BUILDERS, INC.</span>
  </div>
  <div class="front-url">www.kordbuild.com</div>
</section>

<section class="card card--back-right">
  <div class="wordmark">
    <span class="wordmark__name">KORD</span>
    <span class="wordmark__suffix">BUILDERS, INC.</span>
  </div>
  <div class="stripe-v"></div>
  <div class="person">
    <div class="person__name">LEO MARCHETTI</div>
    <div class="person__title">Principal / Vice President</div>
  </div>
  <ul class="contact-stack">
    <li>555-014-2271<span class="ico-box"><svg class="ico" viewBox="0 0 24 24"><path d="M6.6 10.8a15 15 0 006.6 6.6l2.2-2.2c.3-.3.7-.4 1-.2 1.1.4 2.3.6 3.6.6.6 0 1 .4 1 1V20c0 .6-.4 1-1 1A17 17 0 013 4c0-.6.4-1 1-1h3.5c.6 0 1 .4 1 1 0 1.3.2 2.5.6 3.6.1.3 0 .7-.2 1z"/></svg></span></li>
    <li>555-016-3308<span class="ico-box"><svg class="ico" viewBox="0 0 24 24"><path d="M7 1h10a2 2 0 012 2v18a2 2 0 01-2 2H7a2 2 0 01-2-2V3a2 2 0 012-2zm0 3v14h10V4zm5 15.5a1.2 1.2 0 100 2.4 1.2 1.2 0 000-2.4z"/></svg></span></li>
    <li>leo@kordbuild.com<span class="ico-box"><svg class="ico" viewBox="0 0 24 24"><path d="M2 5h20v14H2zm2 2v.5l8 5 8-5V7zm0 3v7h16v-7l-8 5z"/></svg></span></li>
    <li>118 Harbor Line Ave. Linden, NJ 07036<span class="ico-box"><svg class="ico" viewBox="0 0 24 24"><path d="M12 1a8 8 0 018 8c0 6-8 14-8 14S4 15 4 9a8 8 0 018-8zm0 4.5a3.5 3.5 0 100 7 3.5 3.5 0 000-7z"/></svg></span></li>
  </ul>
</section>

<section class="card card--front-dark">
  <div class="wordmark">
    <span class="wordmark__name">KORD</span>
    <span class="wordmark__suffix">BUILDERS, INC.</span>
  </div>
</section>

<section class="card card--back-left">
  <div class="stripe-v"></div>
  <div class="person">
    <div class="person__name">LEO MARCHETTI</div>
    <div class="person__title">Principal / Vice President</div>
  </div>
  <div class="wordmark">
    <span class="wordmark__name">KORD</span>
    <span class="wordmark__suffix">BUILDERS, INC.</span>
  </div>
  <ul class="contact-list">
    <li><svg class="ico" viewBox="0 0 24 24"><path d="M6.6 10.8a15 15 0 006.6 6.6l2.2-2.2c.3-.3.7-.4 1-.2 1.1.4 2.3.6 3.6.6.6 0 1 .4 1 1V20c0 .6-.4 1-1 1A17 17 0 013 4c0-.6.4-1 1-1h3.5c.6 0 1 .4 1 1 0 1.3.2 2.5.6 3.6.1.3 0 .7-.2 1z"/></svg>555-014-2271</li>
    <li><svg class="ico" viewBox="0 0 24 24"><path d="M7 1h10a2 2 0 012 2v18a2 2 0 01-2 2H7a2 2 0 01-2-2V3a2 2 0 012-2zm0 3v14h10V4zm5 15.5a1.2 1.2 0 100 2.4 1.2 1.2 0 000-2.4z"/></svg>555-016-3308</li>
    <li><svg class="ico" viewBox="0 0 24 24"><path d="M2 5h20v14H2zm2 2v.5l8 5 8-5V7zm0 3v7h16v-7l-8 5z"/></svg>leo@kordbuild.com</li>
    <li><svg class="ico" viewBox="0 0 24 24"><path d="M12 2a10 10 0 100 20 10 10 0 000-20zm0 2c.9 0 2.2 2 2.6 5H9.4c.4-3 1.7-5 2.6-5zM4.3 9h3.1a20 20 0 000 6H4.3a8 8 0 010-6zm5.1 0h5.2a18 18 0 010 6H9.4a18 18 0 010-6zm7.2 0h3.1a8 8 0 010 6h-3.1a20 20 0 000-6zM9.4 17h5.2c-.4 3-1.7 5-2.6 5s-2.2-2-2.6-5z"/></svg>www.kordbuild.com</li>
    <li><svg class="ico" viewBox="0 0 24 24"><path d="M12 1a8 8 0 018 8c0 6-8 14-8 14S4 15 4 9a8 8 0 018-8zm0 4.5a3.5 3.5 0 100 7 3.5 3.5 0 000-7z"/></svg><span>118 Harbor Line Avenue<br>Linden, New Jersey 07036</span></li>
  </ul>
</section>

</body>
</html>
```